Specialized Personal Trainer Needs a Business Card Design

I need a business card design for my personal training business called Tall Oak Fitness. I have my Human Kinetics degree in Exercise Science from the Halvern Ridge University as well as an extra certification from NBEP (National Board of Exercise Practice). I work as a Cardiac Rehab Exercise Specialist and personal trainer giving specialized exercise prescriptions to those that have different heart conditions as well as work with the general population in weight loss, strength and conditioning, getting/staying fit.
Updates

I decided that I wanted a logo (as I did not have one before I submitted my project for a business card) so I am submitting a project to get a logo done and then I will decide on a business card, hopefully being able to use one of the designs already submitted.  My apologies for doing this backwards.  I am new to this so I appreciate your patience.

Thank you.

Hi, I have just created a project for a logo design (I realized I needed a logo and I should've done that first..oops!), please feel free to participate.  Once I receive a logo I like I will finalize my business card project and hopefully incorporate it into one of your business card designs. 

Thank you!

Target Market(s)

Business professionals

Industry/Entity Type

Personal Trainer

Requirements
Must have
• My name with my info:
Celia R. Dunhill (BHK)
NBEP Certified Clinical Exercise Specialist & Personal Trainer
celia.dunhill@talloakfitness.example
Cell: 604-358-4170

Please make it double sided.
Nice to have
• An image that represents cardiac and general fitness training.

```html
<!DOCTYPE html>
<html lang="en">
<head>
<meta charset="utf-8">
<title>Tall Oak Fitness — Business Card</title>
<link rel="stylesheet" href="https://fonts.googleapis.com/css2?family=Roboto:wght@400;700;900&display=swap">
<style>
  :root {
    --brand-red: #e3202a;
    --brand-red-deep: #c4161f;
    --surface-light: #f1f1f1;
    --surface-mid: #d9d9d9;
    --ink-gray: #8c8c8c;
    --ink-soft: #9a9a9a;
    --page: #ffffff;
  }
  * { margin: 0; padding: 0; box-sizing: border-box; }
  html, body {
    width: 917px;
    height: 1200px;
    overflow: hidden;
    background: var(--page);
    font-family: "Roboto", Arial, sans-serif;
  }
  .canvas { position: relative; width: 917px; height: 1200px; }

  .card {
    position: absolute;
    left: 0;
    width: 917px;
    overflow: hidden;
  }
  .card--front { top: 0; height: 588px; }
  .card--back { top: 610px; height: 590px; }
  .card__bg { position: absolute; inset: 0; width: 100%; height: 100%; }

  /* Front brand mark */
  .front-brand {
    position: absolute;
    top: 22px;
    right: 70px;
    display: flex;
    align-items: flex-start;
    gap: 22px;
  }
  .front-brand__name {
    color: var(--brand-red);
    font-weight: 900;
    font-size: 56px;
    line-height: 0.95;
    letter-spacing: -1px;
  }
  .front-brand__square {
    width: 46px;
    height: 46px;
    margin-top: 8px;
    background: var(--brand-red);
  }

  /* Back layout */
  .back-brand {
    position: absolute;
    left: 78px;
    top: 175px;
    width: 220px;
    display: flex;
    flex-direction: column;
    gap: 16px;
  }
  .back-brand__name {
    color: var(--brand-red);
    font-weight: 900;
    font-size: 36px;
    line-height: 0.98;
    letter-spacing: -0.5px;
  }
  .back-brand__square {
    width: 34px;
    height: 34px;
    background: var(--brand-red);
  }
  .divider {
    position: absolute;
    left: 334px;
    top: 140px;
    width: 3px;
    height: 258px;
    background: var(--brand-red);
  }
  .contact {
    position: absolute;
    left: 362px;
    top: 196px;
    color: var(--ink-gray);
  }
  .contact__name {
    font-size: 27px;
    font-weight: 700;
    letter-spacing: 0.2px;
  }
  .contact__title {
    margin-top: 14px;
    font-size: 11.5px;
    font-weight: 700;
    color: var(--ink-soft);
  }
  .contact__row {
    display: flex;
    margin-top: 30px;
    font-size: 14px;
    color: var(--ink-soft);
  }
  .contact__row + .contact__row { margin-top: 32px; }
  .contact__label { width: 58px; }
</style>
</head>
<body>
<main class="canvas">

  <section class="card card--front" aria-label="Business card front">
    <svg class="card__bg" viewBox="0 0 917 588" preserveAspectRatio="none" aria-hidden="true">
      <defs>
        <linearGradient id="frontRed" x1="0" y1="0" x2="1" y2="1">
          <stop offset="0" stop-color="#ec2530"/>
          <stop offset="1" stop-color="#c4161f"/>
        </linearGradient>
        <linearGradient id="frontLight" x1="0" y1="0" x2="1" y2="1">
          <stop offset="0" stop-color="#fbfbfb"/>
          <stop offset="1" stop-color="#d6d6d6"/>
        </linearGradient>
      </defs>
      <rect width="917" height="588" fill="url(#frontRed)"/>
      <path d="M70 0 C110 250 340 470 917 545 L917 0 Z" fill="url(#frontLight)"/>
    </svg>
    <div class="front-brand">
      <div class="front-brand__name">Tall Oak<br>Fitness</div>
      <div class="front-brand__square"></div>
    </div>
  </section>

  <section class="card card--back" aria-label="Business card back">
    <svg class="card__bg" viewBox="0 0 917 590" preserveAspectRatio="none" aria-hidden="true">
      <defs>
        <linearGradient id="backLight" x1="0" y1="0" x2="1" y2="1">
          <stop offset="0" stop-color="#e6e6e6"/>
          <stop offset="0.5" stop-color="#f7f7f7"/>
          <stop offset="1" stop-color="#e2e2e2"/>
        </linearGradient>
        <linearGradient id="backRed" x1="0" y1="0" x2="1" y2="0">
          <stop offset="0" stop-color="#ec2530"/>
          <stop offset="1" stop-color="#c4161f"/>
        </linearGradient>
      </defs>
      <rect width="917" height="590" fill="url(#backLight)"/>
      <path d="M0 430 C250 560 600 520 917 440 L917 590 L0 590 Z" fill="url(#backRed)"/>
    </svg>
    <div class="back-brand">
      <div class="back-brand__square"></div>
      <div class="back-brand__name">Tall Oak<br>Fitness</div>
    </div>
    <div class="divider"></div>
    <div class="contact">
      <p class="contact__name">Celia R. Dunhill (BHK)</p>
      <p class="contact__title">NBEP Certified Clinical Exercise Specialist &amp; Personal Trainer</p>
      <p class="contact__row"><span class="contact__label">email</span><span>celia.dunhill@talloakfitness.example</span></p>
      <p class="contact__row"><span class="contact__label">cell</span><span>604-358-4170</span></p>
    </div>
  </section>

</main>
</body>
</html>
```